Recycling company need a brochure - We are metal and electronic recycling company, we need a broc...

We need to illustrate our e-scrap services and values to our costumers in this brochure. We are collecting and recycling electronic waste. We are sorting, and dismanteling the goods to maximize value of the goods. We are using color green on business cards and on our trucks and containers, so brochure should also have green, we are a green business. It should communicate that doing business with us is; simple, easy to establish relations, quick transport service and
enviromental friendly. More info: www.ravnsted-metal.dk

Target Market(s)

Companies with used electronic for scrap / Try go to www.ravnsted-metal.dk to get more info.

Industry/Entity Type

Recycling

Font styles to use
Serif

Requirements
Must have
• Key services:
• Pick up service / Logistics
• Fast report
• Data destruction
• Fast payment
• AAA Credit-logo
• ISO14001 Certifikat-logo
• Company Logo
Nice to have
• Please browse the uploaded pictures, and use your favourites

```html
<!DOCTYPE html>
<html lang="da">
<head>
<meta charset="utf-8">
<title>Ravnsted – Brochure</title>
<link href="https://fonts.googleapis.com/css2?family=Cinzel:wght@600&family=Open+Sans:wght@400;600;700;800&display=swap" rel="stylesheet">
<style>
:root{
  --green:#3fa93a;
  --green-dark:#1f7d34;
  --green-light:#8fcf5a;
  --ink:#3a3a3a;
  --muted:#7a7a7a;
  --paper:#ffffff;
  --stage:#e6e6e6;
  --photo-sky:#7fa7cf;
  --photo-metal:#8a8278;
  --photo-rust:#6f5a48;
  --photo-ewaste:#9aa3a8;
}
*{box-sizing:border-box;margin:0;padding:0}
html,body{width:1200px;height:2400px;overflow:hidden}
body{background:var(--stage);font-family:"Open Sans",Arial,sans-serif;color:var(--ink);
  display:flex;flex-direction:column;align-items:center;justify-content:center;gap:160px}
.spread{display:flex;width:1140px;height:806px;background:var(--paper);box-shadow:0 10px 30px rgba(0,0,0,.12)}
.panel{position:relative;width:380px;height:806px;overflow:hidden;background:var(--paper)}
.panel + .panel{border-left:1px solid #e2e2e2}
.photo{position:absolute;left:0;width:100%}
.photo--scrapyard{background:linear-gradient(180deg,var(--photo-sky) 0%,#b9cde0 30%,var(--photo-metal) 48%,var(--photo-rust) 100%)}
.photo--ewaste{background:linear-gradient(160deg,#c9cfd2 0%,var(--photo-ewaste) 55%,#6e767b 100%)}
.photo--heap{background:linear-gradient(180deg,#a9bccd 0%,#c3c7c9 25%,#8d7f72 60%,var(--photo-rust) 100%)}
.footer-band{position:absolute;left:0;bottom:0;width:100%;height:46px;background:var(--green);
  color:#fff;font-size:13px;font-weight:600;display:flex;align-items:center;justify-content:center;gap:14px;letter-spacing:.5px}
.footer-band svg{width:14px;height:14px;fill:#fff}
.wordmark{display:flex;flex-direction:column;align-items:center;gap:8px}
.wordmark__dot{width:46px;height:46px;border-radius:50%;background:var(--green)}
.wordmark__name{font-family:"Cinzel",Georgia,serif;font-weight:600;font-size:30px;letter-spacing:6px;color:var(--green-dark)}
.wordmark--light .wordmark__dot{background:#fff}
.wordmark--light .wordmark__name{color:#fff}
.ribbon{position:absolute;left:-50px;width:480px;height:96px;background:var(--green);transform:rotate(-24deg);
  color:#fff;font-weight:800;font-size:19px;line-height:1.25;letter-spacing:1px;text-align:center;
  display:flex;align-items:center;justify-content:center;box-shadow:0 4px 10px rgba(0,0,0,.2)}
.ribbon--outline{background:transparent;border:2px solid #fff;box-shadow:none}
.heading{font-size:20px;font-weight:800;color:var(--green-dark);letter-spacing:1px}
.body-text{font-size:11.5px;line-height:1.6;color:var(--muted)}
.service-list{list-style:none;display:flex;flex-direction:column;gap:14px}
.service-list li{display:flex;align-items:center;gap:12px;font-size:12.5px;font-weight:600;color:var(--ink)}
.service-list svg{width:22px;height:22px;flex:none}
.bullets{list-style:none;columns:2;font-size:11px;color:var(--muted);line-height:1.9}
.bullets li::before{content:"";display:inline-block;width:6px;height:6px;background:var(--green);margin-right:8px;vertical-align:middle}
.contact{color:#fff;font-size:12px;line-height:1.9;text-align:center}
.badges{display:flex;gap:16px;justify-content:center}
.badge{width:58px;height:58px;border-radius:50%;background:rgba(255,255,255,.9)}
.badge--square{border-radius:6px}
</style>
</head>
<body>

<section class="spread spread--outside">
  <article class="panel panel--services">
    <div class="photo photo--ewaste" style="top:0;height:230px" role="img" aria-label="Photo of sorted electronic scrap and circuit boards"></div>
    <div style="position:absolute;top:262px;left:34px;right:34px">
      <h2 class="heading" style="margin-bottom:10px">VORES YDELSER</h2>
      <p class="body-text" style="margin-bottom:24px">Vi henter, sorterer og adskiller brugt elektronik, så værdien af jeres materialer bliver så høj som muligt.</p>
      <ul class="service-list">
        <li><svg viewBox="0 0 24 24"><circle cx="12" cy="12" r="12" fill="var(--green)"/><path d="M7 12.5l3 3 7-7" stroke="#fff" stroke-width="2.2" fill="none"/></svg>Afhentning og logistik</li>
        <li><svg viewBox="0 0 24 24"><circle cx="12" cy="12" r="12" fill="var(--green)"/><path d="M7 12.5l3 3 7-7" stroke="#fff" stroke-width="2.2" fill="none"/></svg>Hurtig rapport</li>
        <li><svg viewBox="0 0 24 24"><circle cx="12" cy="12" r="12" fill="var(--green)"/><path d="M7 12.5l3 3 7-7" stroke="#fff" stroke-width="2.2" fill="none"/></svg>Datadestruktion</li>
        <li><svg viewBox="0 0 24 24"><circle cx="12" cy="12" r="12" fill="var(--green)"/><path d="M7 12.5l3 3 7-7" stroke="#fff" stroke-width="2.2" fill="none"/></svg>Hurtig betaling</li>
        <li><svg viewBox="0 0 24 24"><circle cx="12" cy="12" r="12" fill="var(--green)"/><path d="M7 12.5l3 3 7-7" stroke="#fff" stroke-width="2.2" fill="none"/></svg>Miljøvenlig genanvendelse</li>
        <li><svg viewBox="0 0 24 24"><circle cx="12" cy="12" r="12" fill="var(--green)"/><path d="M7 12.5l3 3 7-7" stroke="#fff" stroke-width="2.2" fill="none"/></svg>Enkel og nem kontakt</li>
      </ul>
    </div>
    <div class="footer-band"><span>www.ravnsted-metal.dk</span></div>
  </article>

  <article class="panel panel--back" style="background:var(--green)">
    <div class="ribbon ribbon--outline" style="top:90px;height:80px;font-size:16px">FRA AFFALD TIL<br>RESSOURCEVÆRDI</div>
    <div class="wordmark wordmark--light" style="position:absolute;top:270px;left:0;right:0">
      <span class="wordmark__dot"></span>
      <span class="wordmark__name">RAVNSTED</span>
    </div>
    <div class="contact" style="position:absolute;top:420px;left:0;right:0">
      Ravnsted Genanvendelse A/S<br>
      Industrivej 14<br>
      7100 Vejle<br>
      Tlf. +45 20 40 60 80<br>
      info@ravnsted-metal.dk
    </div>
    <div class="badges" style="position:absolute;top:600px;left:0;right:0">
      <span class="badge"></span><span class="badge badge--square"></span>
    </div>
    <div class="footer-band" style="background:var(--green-dark)">
      <svg viewBox="0 0 24 24"><path d="M6.6 10.8a15 15 0 006.6 6.6l2.2-2.2a1 1 0 011-.25 11.4 11.4 0 003.6.6 1 1 0 011 1V20a1 1 0 01-1 1A17 17 0 013 4a1 1 0 011-1h3.5a1 1 0 011 1 11.4 11.4 0 00.6 3.6 1 1 0 01-.25 1z"/></svg>
      <span>+45 20 40 60 80</span>
    </div>
  </article>

  <article class="panel panel--cover">
    <div class="wordmark" style="position:absolute;top:40px;left:0;right:0">
      <span class="wordmark__dot"></span>
      <span class="wordmark__name">RAVNSTED</span>
    </div>
    <div class="photo photo--scrapyard" style="top:190px;height:570px" role="img" aria-label="Photo of a scrap yard with a material handler lifting metal"></div>
    <div class="ribbon" style="top:520px">FRA AFFALD TIL<br>RESSOURCEVÆRDI</div>
    <div class="footer-band"><span>www.ravnsted-metal.dk</span></div>
  </article>
</section>

<section class="spread spread--inside">
  <article class="panel panel--about">
    <div class="photo photo--ewaste" style="top:0;height:220px" role="img" aria-label="Photo of a recycling hall with stacked electronics"></div>
    <div style="position:absolute;top:250px;left:34px;right:34px">
      <h2 class="heading" style="margin-bottom:12px">OM OS</h2>
      <p class="body-text" style="margin-bottom:12px">Ravnsted er en grøn virksomhed, der indsamler og genanvender metal og elektronisk affald fra virksomheder i hele landet.</p>
      <p class="body-text" style="margin-bottom:20px">Vi gør det enkelt at samarbejde: én kontakt, hurtig transport og en klar rapport efter hver afhentning.</p>
      <ul class="bullets">
        <li>Computere</li><li>Servere</li><li>Printere</li><li>Kabler</li>
        <li>Mobiltelefoner</li><li>Skærme</li><li>Printplader</li><li>Batterier</li>
      </ul>
    </div>
    <div class="footer-band"><span>RING FOR AFHENTNING I DAG</span></div>
  </article>

  <article class="panel panel--process">
    <svg style="position:absolute;top:0;left:0" width="380" height="380" viewBox="0 0 380 380">
      <path d="M0 0H380V300Q190 380 0 300Z" fill="var(--green)"/>
    </svg>
    <h2 class="heading" style="position:absolute;top:34px;left:0;right:0;text-align:center;color:#fff">SÅDAN GØR VI</h2>
    <svg style="position:absolute;top:100px;left:70px" width="240" height="240" viewBox="0 0 240 240" role="img" aria-label="Ring chart of the recycling steps">
      <circle cx="120" cy="120" r="110" fill="#fff"/>
      <g fill="none" stroke-width="42" transform="rotate(-90 120 120)">
        <circle cx="120" cy="120" r="80" stroke="var(--green-dark)" stroke-dasharray="120 383"/>
        <circle cx="120" cy="120" r="80" stroke="var(--green)" stroke-dasharray="120 383" stroke-dashoffset="-126"/>
        <circle cx="120" cy="120" r="80" stroke="var(--green-light)" stroke-dasharray="120 383" stroke-dashoffset="-252"/>
        <circle cx="120" cy="120" r="80" stroke="#bdbdbd" stroke-dasharray="117 383" stroke-dashoffset="-378"/>
      </g>
      <circle cx="120" cy="120" r="52" fill="#fff"/>
      <circle cx="120" cy="120" r="18" fill="var(--green)"/>
    </svg>
    <div style="position:absolute;top:380px;left:34px;right:34px">
      <ul class="service-list" style="gap:12px">
        <li><svg viewBox="0 0 24 24"><rect width="24" height="24" rx="4" fill="var(--green-dark)"/></svg>1. Indsamling</li>
        <li><svg viewBox="0 0 24 24"><rect width="24" height="24" rx="4" fill="var(--green)"/></svg>2. Sortering</li>
        <li><svg viewBox="0 0 24 24"><rect width="24" height="24" rx="4" fill="var(--green-light)"/></svg>3. Adskillelse</li>
        <li><svg viewBox="0 0 24 24"><rect width="24" height="24" rx="4" fill="#bdbdbd"/></svg>4. Genanvendelse</li>
      </ul>
      <p class="body-text" style="margin-top:20px">Hvert trin sikrer den højeste værdi for jeres materialer og den mindste belastning af miljøet.</p>
    </div>
    <div class="footer-band"><span>www.ravnsted-metal.dk</span></div>
  </article>

  <article class="panel panel--values">
    <div class="photo photo--heap" style="top:0;height:300px" role="img" aria-label="Photo of a large pile of scrap metal under a blue sky"></div>
    <div style="position:absolute;top:330px;left:34px;right:34px">
      <h2 class="heading" style="margin-bottom:12px">HVORFOR OS</h2>
      <p class="body-text" style="margin-bottom:12px">Vi tilbyder hurtig betaling, sikker datadestruktion og certificeret håndtering efter gældende miljøkrav.</p>
      <p class="body-text" style="margin-bottom:22px">Kontakt os, så finder vi den løsning, der passer til jeres virksomhed.</p>
      <div class="badges" style="justify-content:flex-start">
        <span class="badge" style="background:var(--green)"></span>
        <span class="badge badge--square" style="background:var(--green-dark)"></span>
      </div>
    </div>
    <div class="footer-band">
      <svg viewBox="0 0 24 24"><path d="M6.6 10.8a15 15 0 006.6 6.6l2.2-2.2a1 1 0 011-.25 11.4 11.4 0 003.6.6 1 1 0 011 1V20a1 1 0 01-1 1A17 17 0 013 4a1 1 0 011-1h3.5a1 1 0 011 1 11.4 11.4 0 00.6 3.6 1 1 0 01-.25 1z"/></svg>
      <span>+45 20 40 60 80</span>
    </div>
  </article>
</section>

</body>
</html>
```